TKA Electricial Contracting Services

Hi guys, after a design for my small electrical company, have logo design files to be incorporated into the layout, the basic concept is electrical contracting services for residential, commercial, industrial & data services, image is clean clear and strong,

Card format is to have a nice clean logo on front,with maybe the Residential – commercial – industrial - data, followed with licensed & insured, followed by contact details on backside of the card.

Target Market(s)

Residential, commercial, industrial sectors.

Industry/Entity Type

Electrical

Contact Information for Business Card

TKA logo,
Residential – commercial – industrial - data
REC: 61372
Email: tka@poralink.net.au
Phone: 0458 203 719

Requirements
Must have
• Clean & strong design.
Nice to have
• If possible, I would like the logo colours inverted so the text is orange and the background is black on the front of the card, then the backside of the card be the reverse colour
Should not have
• No Sparks, lightning bolts,

```html
<!DOCTYPE html>
<html lang="en">
<head>
<meta charset="utf-8">
<title>TKA Electrical – Business Card</title>
<link rel="stylesheet" href="https://fonts.googleapis.com/css2?family=Exo+2:wght@500;600;700&display=swap">
<style>
  :root {
    --page: #eeeeec;
    --orange: #f08a3c;
    --orange-deep: #e07a2e;
    --black: #0c0c0c;
    --charcoal: #1e1e1e;
    --ink: #2a2a2a;
  }
  * { box-sizing: border-box; margin: 0; padding: 0; }
  html, body { width: 1200px; height: 1000px; overflow: hidden; }
  body {
    background: var(--page);
    font-family: "Exo 2", Arial, sans-serif;
    position: relative;
  }
  .card {
    position: absolute;
    left: 220px;
    width: 760px;
    height: 400px;
    border-radius: 4px;
    box-shadow: 0 6px 18px rgba(0,0,0,.18);
    overflow: hidden;
  }
  .card--front {
    top: 70px;
    background: linear-gradient(135deg, var(--orange-deep), var(--orange) 60%, #f5a56a);
    display: flex;
    flex-direction: column;
    align-items: center;
    justify-content: center;
  }
  .front-mark {
    font-weight: 700;
    font-size: 150px;
    line-height: 1;
    color: var(--ink);
    letter-spacing: 2px;
  }
  .front-name {
    font-weight: 600;
    font-size: 30px;
    color: var(--ink);
    margin-top: 6px;
    letter-spacing: 1px;
  }
  .card--back {
    top: 530px;
    background: linear-gradient(120deg, var(--black) 45%, var(--charcoal));
    color: var(--orange);
  }
  .back-brand { position: absolute; left: 62px; top: 80px; }
  .back-mark {
    font-weight: 700;
    font-size: 92px;
    line-height: 1;
    letter-spacing: 2px;
  }
  .back-name {
    font-weight: 600;
    font-size: 20px;
    letter-spacing: 1px;
    margin-top: 4px;
  }
  .services {
    position: absolute;
    left: 64px;
    top: 226px;
    list-style: none;
    font-weight: 600;
    font-size: 18px;
    line-height: 23px;
  }
  .services li { display: flex; align-items: center; gap: 6px; }
  .services li::before {
    content: "";
    width: 6px; height: 6px;
    border-radius: 50%;
    background: var(--orange);
  }
  .credentials {
    position: absolute;
    left: 64px;
    top: 334px;
    font-weight: 500;
    font-size: 15px;
    line-height: 20px;
    letter-spacing: .5px;
  }
  .divider {
    position: absolute;
    left: 412px;
    top: 262px;
    width: 12px;
    height: 120px;
    border-left: 3px solid var(--orange);
    border-right: 3px solid var(--orange);
  }
  .contacts {
    position: absolute;
    left: 444px;
    top: 278px;
    list-style: none;
    font-weight: 500;
    font-size: 21px;
    letter-spacing: 1px;
  }
  .contacts li { display: flex; align-items: center; gap: 10px; height: 42px; }
  .contacts svg { width: 30px; height: 30px; flex: none; }
</style>
</head>
<body>
  <section class="card card--front">
    <div class="front-mark">TKA</div>
    <div class="front-name">Tavish Kane Electrical</div>
  </section>

  <section class="card card--back">
    <div class="back-brand">
      <div class="back-mark">TKA</div>
      <div class="back-name">Tavish Kane Electrical</div>
    </div>

    <ul class="services">
      <li>Residential</li>
      <li>commercial</li>
      <li>industrial</li>
      <li>data</li>
    </ul>

    <div class="credentials">
      <div>Licensed &amp; Insured</div>
      <div>REC: 61372</div>
    </div>

    <div class="divider"></div>

    <ul class="contacts">
      <li>
        <svg viewBox="0 0 30 30" aria-hidden="true">
          <circle cx="15" cy="15" r="13" fill="none" stroke="#f08a3c" stroke-width="2.5"/>
          <path d="M10.5 8.5l3 0 1 3.5-2 1.3c.9 1.9 2.3 3.3 4.2 4.2l1.3-2 3.5 1v3c-6 .5-11.5-5-11-11z" fill="#f08a3c"/>
        </svg>
        <span>0458 203 719</span>
      </li>
      <li>
        <svg viewBox="0 0 30 30" aria-hidden="true">
          <circle cx="15" cy="15" r="13" fill="none" stroke="#f08a3c" stroke-width="2.5"/>
          <rect x="8.5" y="10.5" width="13" height="9" fill="none" stroke="#f08a3c" stroke-width="2"/>
          <path d="M8.5 10.5l6.5 5 6.5-5" fill="none" stroke="#f08a3c" stroke-width="2"/>
        </svg>
        <span>tka@poralink.net.au</span>
      </li>
    </ul>
  </section>
</body>
</html>
```